Redesign of Engineering firm website

I want a redesign of the velkorpower.com website with the below in mind:

1- the client has a 3 main sectors: Renewable Energy, Process Automation and General Engineering.
2- Home page should show the 3 sectors
3- the other standard pages should be home, About, Clients, Projects, Training, Career, and Contact
4- The theme should be wordpress.
5- Responsive layout that works with all devices
6- One page layout is preferable for the home page.
7- it should be original and is not copied from other templates.

Target Market(s)

Engineers and professional

Industry/Entity Type

Solar Energy

Font styles to use
Serif
Sans Serif

Colors
3277b5
0355a3
0493ce

Requirements
Must have
• pictures that represent the three sectors

```html
<!DOCTYPE html>
<html lang="en">
<head>
<meta charset="utf-8">
<title>Velkor — Solar Energy Engineering</title>
<link rel="stylesheet" href="https://fonts.googleapis.com/css2?family=Montserrat:wght@500;600;700&family=Roboto:wght@500;700&family=Arimo:wght@400;700&family=Tinos&family=Quicksand:wght@500;600&display=swap">
<style>
  :root {
    --blue-deep: #0355a3;
    --blue-mid: #3277b5;
    --blue-bright: #0493ce;
    --blue-title: #2b60c8;
    --text-grey: #555a60;
    --news-bg: #f1f1f1;
    --footer-bg: #2c2f34;
    --footer-text: #e8ecef;
    --white: #ffffff;
  }
  * { box-sizing: border-box; margin: 0; padding: 0; }
  html, body { width: 1200px; height: 2797px; overflow: hidden; }
  body { position: relative; background: var(--white); font-family: "Arimo", Arial, sans-serif; color: var(--text-grey); }

  /* Header */
  .site-header { position: absolute; left: 0; top: 0; width: 1200px; height: 148px; background: var(--white); }
  .brand { position: absolute; left: 42px; top: 50px; display: flex; align-items: center; gap: 10px; }
  .brand-mark { width: 20px; height: 20px; background: var(--blue-bright); border-radius: 50%; flex: none; }
  .brand-name { font-family: "Montserrat", sans-serif; font-weight: 700; font-size: 44px; letter-spacing: 1px; color: var(--blue-bright); line-height: 1; }
  .main-nav { position: absolute; left: 389px; top: 68px; width: 710px; display: flex; justify-content: space-between; }
  .main-nav a { font-family: "Montserrat", sans-serif; font-weight: 600; font-size: 22px; color: var(--blue-bright); text-decoration: none; line-height: 36px; white-space: nowrap; }
  .main-nav a.active { color: var(--blue-deep); border-bottom: 3px solid var(--blue-deep); }
  .menu-toggle { position: absolute; left: 1133px; top: 72px; width: 33px; }
  .menu-toggle span { display: block; height: 4px; margin-bottom: 6px; background: var(--blue-deep); border-radius: 2px; }

  /* Hero */
  .hero { position: absolute; left: 0; top: 148px; width: 1200px; height: 420px;
    background: linear-gradient(180deg, #8ba2b8 0%, #c2cad0 35%, #5f7590 52%, #25407a 70%, #13285a 100%); }
  .hero-title { position: absolute; left: 0; width: 1200px; top: 206px; text-align: center; font-family: "Montserrat", sans-serif; font-weight: 500; font-size: 62px; line-height: 76px; color: var(--white); }
  .hero-dots { position: absolute; left: 1073px; top: 392px; display: flex; gap: 7px; }
  .hero-dots span { width: 13px; height: 13px; border-radius: 50%; border: 2px solid var(--white); }
  .hero-dots span.on { background: var(--white); }

  /* Section titles */
  .section-title { position: absolute; left: 0; width: 1200px; text-align: center; font-family: "Montserrat", sans-serif; font-weight: 700; font-size: 44px; color: var(--blue-title); }
  .section-lead { position: absolute; left: 87px; width: 1026px; text-align: center; font-size: 18px; line-height: 25px; color: var(--text-grey); }

  /* Services */
  .service { position: absolute; width: 360px; text-align: center; }
  .service-icon { width: 168px; height: 168px; margin: 0 auto; border-radius: 50%; background: var(--blue-deep); display: flex; align-items: center; justify-content: center; }
  .service-label { margin-top: 30px; font-family: "Roboto", sans-serif; font-weight: 500; font-size: 19px; line-height: 24px; color: var(--blue-mid); text-transform: uppercase; }

  /* Sectors band */
  .sectors { position: absolute; left: 0; top: 1309px; width: 1200px; height: 355px;
    background: linear-gradient(160deg, #1e2c3c 0%, #3d5168 35%, #6d7f8f 60%, #8a7660 80%, #47505a 100%); }
  .sector-list { position: absolute; left: 299px; top: 82px; list-style: none; }
  .sector-list li { font-family: "Roboto", sans-serif; font-weight: 700; font-size: 56px; line-height: 84px; color: var(--white); }
  .sector-list li .dot { color: var(--blue-bright); }

  /* News */
  .news { position: absolute; left: 0; top: 1916px; width: 1200px; height: 411px; background: var(--news-bg); }
  .news-item { position: absolute; top: 110px; width: 370px; }
  .news-item h3 { font-family: "Montserrat", sans-serif; font-weight: 700; font-size: 24px; line-height: 34px; color: var(--blue-bright); height: 68px; overflow: hidden; }
  .news-rule { width: 92px; height: 7px; background: var(--blue-deep); margin: 12px 0 16px; }
  .news-item p { font-size: 18px; line-height: 23px; color: var(--text-grey); width: 310px; height: 145px; }
  .read-more { display: inline-block; border: 2px solid var(--blue-mid); padding: 3px 8px; font-family: "Tinos", serif; font-size: 18px; color: var(--blue-mid); text-decoration: none; background: var(--white); }

  /* Footer */
  .site-footer { position: absolute; left: 0; top: 2327px; width: 1200px; height: 470px; background: var(--footer-bg); font-family: "Quicksand", sans-serif; }
  .footer-col { position: absolute; }
  .footer-col h4 { font-family: "Montserrat", sans-serif; font-weight: 600; font-size: 28px; color: var(--blue-bright); margin-bottom: 18px; white-space: nowrap; }
  .footer-col ul { list-style: none; }
  .footer-col li { font-size: 21px; font-weight: 500; color: var(--footer-text); line-height: 46px; }
  .social-links { display: flex; gap: 14px; flex-wrap: wrap; width: 240px; }
  .social-links a { display: inline-flex; align-items: center; gap: 6px; font-size: 18px; font-weight: 600; color: var(--footer-text); text-decoration: none; line-height: 34px; }
  .social-links a i { width: 14px; height: 14px; background: var(--footer-text); border-radius: 3px; display: inline-block; }
  .footer-brand { position: absolute; left: 931px; top: 86px; display: flex; align-items: center; gap: 10px; }
  .footer-brand .brand-name { font-size: 44px; }
  .copyright { position: absolute; left: 940px; top: 200px; font-family: "Arimo", sans-serif; font-size: 21px; line-height: 26px; color: var(--footer-text); }
  .subscribe { position: absolute; left: 640px; top: 295px; }
  .subscribe h4 { font-family: "Montserrat", sans-serif; font-weight: 600; font-size: 28px; color: var(--blue-bright); margin-bottom: 20px; }
  .subscribe-form { display: flex; }
  .subscribe-form .field { width: 185px; height: 40px; background: var(--white); font-family: "Arimo", sans-serif; font-size: 13px; color: #8a8f95; padding: 12px 8px; }
  .subscribe-form .go { width: 42px; height: 40px; background: var(--blue-bright); display: flex; align-items: center; justify-content: center; }
  .to-top { position: absolute; left: 1130px; top: 403px; width: 42px; height: 42px; border-radius: 50%; border: 3px solid var(--blue-bright); display: flex; align-items: center; justify-content: center; }
</style>
</head>
<body>

<header class="site-header">
  <div class="brand"><span class="brand-mark"></span><span class="brand-name">VELKOR</span></div>
  <nav class="main-nav">
    <a class="active" href="#">HOME</a>
    <a href="#">ABOUT</a>
    <a href="#">SERVICES</a>
    <a href="#">PROJECTS</a>
    <a href="#">CLIENTS</a>
    <a href="#">CONTACT</a>
  </nav>
  <div class="menu-toggle"><span></span><span></span><span></span></div>
</header>

<section class="hero" role="img" aria-label="Wind turbines on a hazy horizon above rows of blue solar panels">
  <h1 class="hero-title">We are the solar experts<br>in the solar kingdom</h1>
  <div class="hero-dots"><span class="on"></span><span></span><span></span></div>
</section>

<h2 class="section-title" style="top:608px;">SERVICES</h2>
<p class="section-lead" style="top:676px;">We provides Solar Energy consulting services, Energy Efficiency Consulting services and Data Collection function. With services spanning the entire project lifecycle, Velkor scope goes beyond engineering, procurement and construction.</p>

<div class="service" style="left:19px; top:747px;">
  <div class="service-icon">
    <svg width="100" height="100" viewBox="0 0 100 100" fill="none" stroke="#fff" stroke-width="4">
      <path d="M28 14 H84 L72 66 H16 Z" fill="#fff"/>
      <path d="M45 14 L36 66 M64 14 L55 66 M24 31 H80 M20 48 H76" stroke="#0355a3" stroke-width="3"/>
      <path d="M46 66 V84 M32 86 H62" stroke-width="5"/>
    </svg>
  </div>
  <div class="service-label">Solar Consulting Services</div>
</div>
<div class="service" style="left:399px; top:747px;">
  <div class="service-icon">
    <svg width="100" height="100" viewBox="0 0 100 100" fill="none" stroke="#fff" stroke-width="5">
      <path d="M48 18 H18 V82 H82 V52"/>
      <path d="M30 26 L70 66 M70 40 V66 H44"/>
    </svg>
  </div>
  <div class="service-label">Design and Engineering<br>Development</div>
</div>
<div class="service" style="left:763px; top:747px;">
  <div class="service-icon">
    <svg width="100" height="100" viewBox="0 0 100 100" fill="none" stroke="#fff" stroke-width="4">
      <path d="M18 14 V84 H88"/>
      <path d="M30 70 L46 46 L60 60 L80 26"/>
      <circle cx="30" cy="70" r="5" fill="#fff"/><circle cx="46" cy="46" r="5" fill="#fff"/>
      <circle cx="60" cy="60" r="5" fill="#fff"/><circle cx="80" cy="26" r="5" fill="#fff"/>
    </svg>
  </div>
  <div class="service-label">Feasibility Studies</div>
</div>

<div class="service" style="left:19px; top:1012px;">
  <div class="service-icon">
    <svg width="110" height="110" viewBox="0 0 100 100">
      <path fill="#fff" d="M43 6h14l2 12 8 3 10-7 10 10-7 10 3 8 12 2v14l-12 2-3 8 7 10-10 10-10-7-8 3-2 12H43l-2-12-8-3-10 7-10-10 7-10-3-8-12-2V43l12-2 3-8-7-10 10-10 10 7 8-3z"/>
      <circle cx="50" cy="50" r="16" fill="#0355a3"/>
    </svg>
  </div>
  <div class="service-label">RFP and RFQ Development</div>
</div>
<div class="service" style="left:399px; top:1012px;">
  <div class="service-icon">
    <svg width="100" height="100" viewBox="0 0 100 100">
      <path fill="#fff" d="M82 14a22 22 0 0 0-28 27L16 79a8 8 0 0 0 11 11l38-38a22 22 0 0 0 27-28L80 36 68 34 66 22z"/>
    </svg>
  </div>
  <div class="service-label">Solar System Operations<br>&amp; Maintenance and Monitoring</div>
</div>
<div class="service" style="left:763px; top:1012px;">
  <div class="service-icon">
    <svg width="100" height="100" viewBox="0 0 100 100" fill="none" stroke="#fff" stroke-width="4">
      <path d="M70 54 V86 H20 V14 H70 V30"/>
      <path d="M30 30 H60 M30 42 H58 M30 54 H50 M30 66 H44"/>
      <path d="M82 30 L56 66 L52 78 L62 72 L88 36 Z" fill="#fff"/>
    </svg>
  </div>
  <div class="service-label">Due Diligence Services</div>
</div>

<section class="sectors" role="img" aria-label="Construction cranes against an evening sky representing the three sectors">
  <ul class="sector-list">
    <li>RENEWABLE ENERGY<span class="dot">.</span></li>
    <li>PROCESS AUTOMATION<span class="dot">.</span></li>
    <li>GENERAL ENGINEERING<span class="dot">.</span></li>
  </ul>
</section>

<h2 class="section-title" style="top:1690px;">ABOUT US</h2>
<p class="section-lead" style="top:1768px; left:100px; width:1000px;">We are the solar experts in the solar kingdom. The KSA (Saudi Arabia) solar market is a promising market with huge potential. The plan is to build 41,000 MW of solar in the coming 20 years, as announced by N.S.E.A. (National Solar Energy Authority).</p>

<section class="news">
  <h2 class="section-title" style="top:16px;">RECENT NEWS</h2>
  <article class="news-item" style="left:87px;">
    <h3>Global Conference<br>Visit</h3>
    <div class="news-rule"></div>
    <p>Aliquam interdum commodo cursus. Fusce interdum lacinia tristique. Proin pellentesque quam lacus, sed egestas urna tristique sed. Quisque molestie vitae ex in lobortis.</p>
    <a class="read-more" href="#">Read More</a>
  </article>
  <article class="news-item" style="left:448px;">
    <h3>Website is launched</h3>
    <div class="news-rule"></div>
    <p>Cras eget semper urna. Duis blandit, lectus a convallis tempus, erat lectus ultrices urna, ac interdum velit lorem blandit massa. Vivamus eget purus ante</p>
    <a class="read-more" href="#">Read More</a>
  </article>
  <article class="news-item" style="left:803px;">
    <h3>Annual Meeting is being<br>Held during January</h3>
    <div class="news-rule"></div>
    <p>Pellentesque aliquam, est ut scelerisque tincidunt, quam enim viverra felis, sed cursus sem sapien vel nisl.</p>
    <a class="read-more" href="#">Read More</a>
  </article>
</section>

<footer class="site-footer">
  <div class="footer-col" style="left:67px; top:68px;">
    <h4>FEATURES</h4>
    <ul><li>Home</li><li>Services</li><li>Clients</li><li>Projects</li></ul>
  </div>
  <div class="footer-col" style="left:341px; top:72px;">
    <h4>LEARN MORE</h4>
    <ul><li>Terms</li><li>About</li><li>Contact Us</li><li>Careers</li><li>Training</li></ul>
  </div>
  <div class="footer-col" style="left:630px; top:72px;">
    <h4>SOCIAL CONNECT</h4>
    <div class="social-links">
      <a href="#"><i></i>Facepage</a>
      <a href="#"><i></i>Chirpline</a>
      <a href="#"><i></i>Snapframe</a>
      <a href="#"><i></i>Vidstream</a>
    </div>
  </div>
  <div class="footer-brand"><span class="brand-mark"></span><span class="brand-name">VELKOR</span></div>
  <p class="copyright">© Copyright 2017<br>All Rights Reserved.</p>
  <div class="subscribe">
    <h4>SUBSCRIBE</h4>
    <div class="subscribe-form">
      <div class="field">Enter Your Email</div>
      <div class="go"><svg width="20" height="18" viewBox="0 0 20 18" fill="none" stroke="#fff" stroke-width="3"><path d="M0 9 H17 M10 2 L17 9 L10 16"/></svg></div>
    </div>
  </div>
  <a class="to-top" href="#"><svg width="20" height="14" viewBox="0 0 20 14" fill="none" stroke="#0493ce" stroke-width="3"><path d="M2 12 L10 4 L18 12"/></svg></a>
</footer>

</body>
</html>
```